Trondel Group letterhead

Hi,

I need a letterhead template created for our business. This should be done in word format and A4 size. The images need to not move in the template ie when I am adding writing in etc. and should flow on when I get to a second page.

I have attached our logo templates below.

Other details to include on the letterhead somewhere are:

0438 571 962
Max@Trondelelectrical.example.com.au
PO Box 781 Marrowdale NSW 2163
ABN: 57 318 492 076

Thanks!

```html
<!DOCTYPE html>
<html lang="en">
<head>
<meta charset="utf-8">
<title>Trondel Group Letterhead</title>
<link rel="stylesheet" href="https://fonts.googleapis.com/css2?family=Arimo:wght@400;700&family=Mulish:wght@700;800&display=swap">
<style>
  :root {
    --backdrop: #e2e2e2;
    --paper: #ffffff;
    --ink: #444444;
    --ink-dark: #1d1d1d;
    --accent: #f05a0f;
    --rule: #555555;
  }
  * { box-sizing: border-box; margin: 0; padding: 0; }
  html, body {
    width: 1153px; height: 1200px; overflow: hidden;
    background: var(--backdrop);
  }
  .letterhead {
    position: absolute; left: 152px; top: 0;
    width: 849px; height: 1200px;
    background: var(--paper);
    font-family: "Arimo", Arial, sans-serif;
    color: var(--ink);
  }
  .brand {
    position: absolute; left: 70px; top: 58px; width: 214px;
    display: flex; flex-direction: column; align-items: center; gap: 12px;
  }
  .brand-mark {
    width: 64px; height: 64px; border-radius: 50%;
    border: 6px solid var(--ink-dark);
  }
  .brand-name {
    font-family: "Arimo", Arial, sans-serif;
    font-weight: 700; font-size: 22px; letter-spacing: 1px;
    color: var(--ink-dark); white-space: nowrap;
  }
  .contact {
    position: absolute; left: 565px; top: 66px; height: 97px;
    border-left: 2px solid var(--rule);
    padding-left: 12px;
    font-size: 14px; line-height: 17.4px;
  }
  .contact p { white-space: nowrap; }
  .contact .address { margin-bottom: 8px; }
  .contact .line { display: flex; align-items: center; gap: 4px; }
  .contact svg { width: 11px; height: 11px; fill: var(--accent); }
  .contact .label { color: var(--accent); }
  .salutation {
    position: absolute; left: 77px; top: 368px;
    font-family: "Mulish", "Century Gothic", sans-serif;
    font-weight: 800; font-size: 20px; color: var(--ink);
  }
  .body-copy {
    position: absolute; left: 76px; top: 425px; width: 700px;
    font-size: 14.3px; line-height: 17.4px;
  }
  .body-copy p { margin-bottom: 15px; }
  .closing {
    position: absolute; left: 77px; top: 785px;
    font-family: "Mulish", sans-serif; font-weight: 800; font-size: 11px;
    color: var(--ink-dark);
  }
  .signature {
    position: absolute; left: 71px; top: 838px; width: 104px; height: 32px;
    background: linear-gradient(90deg, #d8d8d8, #ececec);
    border-radius: 3px;
  }
  .footer-band {
    position: absolute; left: 0; top: 1148px; width: 100%; height: 26px;
    display: flex;
  }
  .footer-band .dark { width: 717px; background: var(--ink-dark); }
  .footer-band .bright { flex: 1; background: var(--accent); }
  .footer-mark {
    position: absolute; left: 708px; top: 1134px;
    width: 52px; height: 52px; border-radius: 50%;
    background: var(--paper); border: 4px solid var(--ink-dark);
  }
</style>
</head>
<body>
  <main class="letterhead">
    <header>
      <div class="brand">
        <div class="brand-mark"></div>
        <div class="brand-name">TRONDEL GROUP</div>
      </div>
      <address class="contact" style="font-style:normal">
        <p>PO Box 781</p>
        <p class="address">Marrowdale NSW 2163</p>
        <p class="line">
          <svg viewBox="0 0 24 24" aria-hidden="true"><path d="M3 9c0-3 4-5 9-5s9 2 9 5v2h-5V9c-1-1-7-1-8 0v2H3zm3 3h12l2 8H4z"/></svg>
          0438 571 962
        </p>
        <p class="line">
          <svg viewBox="0 0 24 24" aria-hidden="true"><path d="M2 6h20v13H2zm2 2v1l8 5 8-5V8l-8 5z"/></svg>
          Max@Trondelelectrical.example.com.au
        </p>
        <p><span class="label">ABN:</span> 57 318 492 076</p>
      </address>
    </header>

    <h1 class="salutation">Dear Mr. Harlow,</h1>

    <section class="body-copy">
      <p>Lorem ipsum dolor sit amet, consectetuer adipiscing elit, sed diam nonummy nibh euismod tincidunt ut laor eet dolore magna aliquam erat volutpat. Ut wisi enim ad minim veniam, quis nostrud exerci tationmcorper suscipit lobortis nisl ut aliquip ex ea commodo consequat. Duis autem vel eum iriure dolor in hendrerit in vulputate velit esse molestie consequat, vel illum dolore eu feugiat</p>
      <p>Rorem ipsum dolor sit amet, consectetuer adipiscing elit, sed diam nonummy nibh euismod tincidunt ut laor eet dolore magna aliquam erat volutpat. Ut wisi enim ad minim veniam, quis nostrud exerci tationmcorper suscipit lobortis nisl ut aliquip ex ea commodo consequat. Duis autem vel eum iriure dolor in hendrerit in vulputate velit esse molest</p>
      <p>Dorem ipsum dolor sit amet, consectetuer adipiscing elit, sed diam nonummy nibh euismod tincidunt ut laor eet dolore magna aliquam erat volutpat. Ut wisi enim ad minim veniam, quis nostrud exerci tationmcorper suscipit lobortis nisl ut aliquip ex ea commodo consequat. Duis autem vel eum iriure dolor in hendrerit in suscipit lobortis nisl ut aliquip ex ea commodo consequat. Duis autem vel eum iriure dolor in hendrerit in vulputate velit esse molestie consequat, vel illum</p>
      <p>Sorem ipsum dolor sit amet, consectetuer adipiscing elit, sed diam nonummy nibh euismod tincidunt ut laor eet dolore magna aliquam erat volutpat. Ut wisi enim ad minim veniam, quis nostrud exerci tationmcorper suscipit lobortis nisl ut aliquip ex ea commodo consequat. Duis autem vel eum iriure dolor in</p>
    </section>

    <p class="closing">Sincerely,</p>
    <div class="signature" role="img" aria-label="Handwritten signature"></div>

    <footer>
      <div class="footer-band"><div class="dark"></div><div class="bright"></div></div>
      <div class="footer-mark"></div>
    </footer>
  </main>
</body>
</html>
```